Marlow Hire IT Recruiting firm needs a business card design for Recruiters, Sourcers, and Account

We need business cards that allow us to change all contact info, names, titles (Recruiter, Sourcer, Account Manager, Director, CEO, etc) per person since we have three offices, in three cities, Phoenix, Austin, and Las Vegas. We do recruiting and contractors for IT positions (Developers, Architects, Software Engineers, Security Engineers, Help Desk, DBAs, PMs, Scrum Masters, etc.) Our client companies are very diverse from Meridex 100 to silicone Valley type start-ups.

So, while we what hip, techie, and quirky, it still needs to be professional. Primary color we use is blue, with silver as a secondary color.

Target Market(s)

IT, Technology

Industry/Entity Type

Business

Contact Information for Business Card

Company name: Marlow Hire, Inc.
Website: www.marlowhire-example.com
Logos for Workvine, Blurtly, and Gathra

Name, Title, Office Number, Cell Number, email

Font styles to use
Serif
Sans Serif

Colors
0455a3
d5d5d5

Requirements
Nice to have
• The grey I selected below is not necessary - but, would like silver included. I included a card design (File 3: MHI early trial example.jpg) that I had started on. It's very rough, and not quite what we're looking for, but what we did like is the logo, big, maybe a bit faded, off center, goes out of frame, etc. Still looking for other ideas - you are the pros! But, just an idea of a design element we liked.

```html
<!DOCTYPE html>
<html lang="en">
<head>
<meta charset="utf-8">
<title>Marlow Hire — Business Card</title>
<link rel="stylesheet" href="https://fonts.googleapis.com/css2?family=Cormorant+Garamond:wght@500;600&family=Open+Sans:wght@400;600&display=swap">
<style>
  :root {
    --blue: #0455a3;
    --blue-deep: #0b4d9c;
    --blue-mid: #0a6cbb;
    --blue-line: #39b4f0;
    --silver: #d5d5d5;
    --silver-dark: #a9a9a9;
    --ink: #222428;
    --ink-soft: #555a60;
    --white: #ffffff;
    --page: #e7e9ec;
  }
  * { box-sizing: border-box; margin: 0; padding: 0; }
  html, body { width: 1200px; height: 900px; overflow: hidden; }
  body {
    background: var(--page);
    font-family: "Open Sans", Arial, sans-serif;
    position: relative;
  }
  .card {
    position: absolute;
    left: 250px;
    width: 700px;
    height: 400px;
    border-radius: 22px;
    overflow: hidden;
    box-shadow: 0 10px 28px rgba(0,0,0,.18);
  }
  .card--back { top: 30px; background: linear-gradient(135deg, var(--blue) 0%, var(--blue-deep) 100%); }
  .card--front { top: 470px; background: var(--white); }
  .card__art { position: absolute; inset: 0; width: 100%; height: 100%; }

  .wordmark {
    font-family: "Cormorant Garamond", Georgia, serif;
    font-weight: 600;
    letter-spacing: 3px;
    white-space: nowrap;
  }
  .descriptor {
    font-family: "Open Sans", Arial, sans-serif;
    font-weight: 400;
    letter-spacing: .5px;
    white-space: nowrap;
  }

  /* back */
  .back-brand { position: absolute; left: 150px; top: 130px; color: var(--white); }
  .back-brand .wordmark { font-size: 50px; line-height: 1; }
  .back-brand .descriptor { font-size: 15px; margin-top: 12px; opacity: .85; }
  .back-brand .site { font-size: 22px; margin-top: 14px; letter-spacing: .5px; }

  /* front */
  .front-brand { position: absolute; right: 40px; top: 36px; text-align: right; }
  .front-brand .wordmark { font-size: 36px; color: var(--ink); line-height: 1; }
  .front-brand .descriptor { font-size: 12px; color: var(--ink-soft); margin-top: 8px; }
  .address {
    position: absolute; right: 40px; top: 104px; text-align: right;
    font-size: 15px; line-height: 1.35; color: var(--ink); font-style: normal;
  }
  .person { position: absolute; left: 50px; top: 166px; }
  .person__name { font-size: 24px; color: var(--blue); font-weight: 400; letter-spacing: .3px; line-height: 1.2; }
  .person__title { font-size: 16px; color: var(--ink); font-weight: 600; line-height: 1.3; }
  .contacts { position: absolute; left: 58px; top: 272px; list-style: none; color: var(--white); font-size: 17px; }
  .contacts li { display: flex; align-items: center; gap: 12px; height: 27px; }
  .contacts svg { width: 15px; height: 15px; flex: none; fill: var(--white); }
  .socials { position: absolute; right: 40px; top: 212px; list-style: none; color: var(--white); font-size: 17px; text-align: right; }
  .socials li { display: flex; justify-content: flex-end; align-items: center; gap: 8px; height: 28px; }
  .socials .chip { width: 15px; height: 15px; border-radius: 3px; background: var(--white); opacity: .85; flex: none; }
</style>
</head>
<body>

<section class="card card--back" aria-label="Card back">
  <svg class="card__art" viewBox="0 0 700 400" aria-hidden="true">
    <circle cx="560" cy="140" r="190" fill="#ffffff" opacity=".06"/>
    <line x1="470" y1="300" x2="700" y2="300" stroke="var(--blue-line)" stroke-width="1.5"/>
    <line x1="0" y1="330" x2="120" y2="330" stroke="var(--blue-line)" stroke-width="1.5"/>
  </svg>
  <div class="back-brand">
    <div class="wordmark">MARLOW HIRE</div>
    <div class="descriptor">IT Recruiting &amp; Contract Talent</div>
    <div class="site">www.marlowhire-example.com</div>
  </div>
</section>

<section class="card card--front" aria-label="Card front">
  <svg class="card__art" viewBox="0 0 700 400" aria-hidden="true">
    <defs>
      <linearGradient id="silverBand" x1="0" y1="0" x2="1" y2="0">
        <stop offset="0" stop-color="var(--silver)"/>
        <stop offset=".5" stop-color="var(--silver-dark)"/>
        <stop offset="1" stop-color="var(--silver)"/>
      </linearGradient>
    </defs>
    <polygon points="0,243 700,163 700,176 0,256" fill="url(#silverBand)"/>
    <polygon points="0,256 700,176 700,400 0,400" fill="var(--blue-mid)"/>
    <polygon points="96,245 126,241 104,266" fill="var(--white)"/>
    <circle cx="600" cy="250" r="110" fill="#ffffff" opacity=".06"/>
  </svg>

  <div class="front-brand">
    <div class="wordmark">MARLOW HIRE</div>
    <div class="descriptor">IT Recruiting &amp; Contract Talent</div>
  </div>
  <address class="address">
    4410 E Cactus Ridge Rd, Suite 210<br>Phoenix, AZ 85000, USA
  </address>

  <div class="person">
    <div class="person__name">YOUR NAME</div>
    <div class="person__title">Title</div>
  </div>

  <ul class="contacts">
    <li><svg viewBox="0 0 16 16"><path d="M3.2 1.5l2.4 2.6-1.3 1.8c.9 2 2.6 3.7 4.6 4.6l1.8-1.3 2.6 2.4-1.4 2.2C7 13.5 2.5 9 1 3z"/></svg>555| 014-2290</li>
    <li><svg viewBox="0 0 16 16"><path d="M4 0h8v16H4zM5.5 2v10h5V2zM7 13.3h2v1.2H7z" fill-rule="evenodd"/></svg>555| 014-2291</li>
    <li><svg viewBox="0 0 16 16"><path d="M1 3h14v10H1zm1.5 1.5L8 9l5.5-4.5v-.2h-11z" fill-rule="evenodd"/></svg>alex@marlowhire-example.com</li>
    <li><svg viewBox="0 0 16 16"><path d="M8 1a7 7 0 100 14A7 7 0 008 1zm0 1.5c.8 0 1.7 1.5 2 3.5H6c.3-2 1.2-3.5 2-3.5zM2.6 6h2c-.1.7-.1 1.3-.1 2s0 1.3.1 2h-2a5.6 5.6 0 010-4zm3.4 0h4c.1.6.1 1.3.1 2s0 1.4-.1 2H6c-.1-.6-.1-1.3-.1-2s0-1.4.1-2zm5.4 0h2a5.6 5.6 0 010 4h-2c.1-.7.1-1.3.1-2s0-1.3-.1-2zM6 11.5h4c-.3 1.9-1.2 3-2 3s-1.7-1.1-2-3z"/></svg>www.marlowhire-example.com</li>
  </ul>

  <ul class="socials">
    <li><span class="chip"></span>Workvine @marlowhire</li>
    <li><span class="chip"></span>Blurtly @marlowhire</li>
    <li><span class="chip"></span>Gathra @marlowhire</li>
  </ul>
</section>

</body>
</html>
```